Bluefinch Painting needs a Website

We need a website built for a Painting company I own, we mainly do residential painting, but don't want to be limited to that.

Need to have estimate request form.
Need pic's of past projects

I like the look of the website for http://www.harborline-painters.example
& "Wexley Property inspections"

My logo that was designed here on ArtHive on the front page

I would like one of the houses I downloaded as part of the background
of the front page.

Target Market(s)

Home owners

Industry/Entity Type

Painting

Number of Pages Required

1 page

Font styles to use
Serif

Requirements
Must have
• Estimate request form for home owners to fill out -
• Name:
• Phone Number:
• Address:
• E-mail:
• Painting project description:
• And my info to:
• My phone number: (555) 318-7046
• My web address bluefinchpainting.example
Nice to have
• My logo that was designed here on ArtHive

```html
<!DOCTYPE html>
<html lang="en">
<head>
<meta charset="utf-8">
<title>Bluefinch Painting</title>
<link href="https://fonts.googleapis.com/css2?family=Open+Sans:wght@300;400;600;700&display=swap" rel="stylesheet">
<style>
:root{
  --blue:#1e8fd6;
  --blue-deep:#1a6fb0;
  --navy:#1d4f80;
  --ink:#2b2b2b;
  --muted:#777;
  --light:#f3f3f3;
  --white:#fff;
  --line:#d9d9d9;
}
*{box-sizing:border-box;margin:0;padding:0}
html,body{width:1200px;height:3000px;overflow:hidden}
body{font-family:"Open Sans",Arial,sans-serif;color:var(--ink);background:var(--white);position:relative}
.abs{position:absolute}
.ph{position:absolute}

/* header */
.header{left:0;top:0;width:1200px;height:96px;background:var(--white)}
.brand{left:216px;top:24px;display:flex;align-items:center;gap:12px}
.brand-mark{width:42px;height:42px;background:var(--navy)}
.brand-name{font-size:30px;font-weight:600;color:var(--navy);letter-spacing:1px}
.help{right:210px;top:24px;text-align:right}
.help-line{font-size:20px;color:var(--ink)}
.help-line b{color:var(--blue);font-weight:400;font-style:italic;font-size:26px}
.help-sub{font-size:11px;color:var(--muted);margin-top:2px}

/* nav */
.nav{left:0;top:96px;width:1200px;height:48px;background:var(--blue)}
.nav a{position:absolute;top:0;height:48px;line-height:48px;color:var(--white);text-decoration:none;font-size:17px;text-align:center}
.nav .active{background:#d7dde3;color:#4a5560;border-top:3px solid #eef1f4}
.nav .cta{top:9px;height:30px;line-height:26px;border:2px solid var(--white);font-weight:600;font-size:16px}

/* hero */
.hero{left:0;top:144px;width:1200px;height:378px;background:linear-gradient(180deg,#b8d6ef 0%,#8fa7b8 35%,#5d6a5a 70%,#7d8a72 100%)}
.hero-title{left:222px;top:276px}
.hero-title span{display:inline-block;background:rgba(30,143,214,.9);color:var(--white);font-size:34px;font-weight:600;padding:0 10px;line-height:44px;margin-bottom:4px}
.dots{left:588px;top:492px;display:flex;gap:6px}
.dots i{width:8px;height:8px;border-radius:50%;background:#fff;opacity:.6}
.dots i:first-child{opacity:1}

/* intro */
.intro{left:0;top:522px;width:1200px;height:333px;background:var(--blue)}
.intro h2{left:219px;top:24px;color:var(--white);font-size:38px;font-weight:700;line-height:44px}
.intro h2 span{font-weight:300;display:block}
.intro p{left:219px;top:138px;width:384px;color:#e6f2fb;font-size:11px;line-height:15px}
.btn-outline{border:1px solid var(--white);color:var(--white);font-size:12px;text-align:center;width:126px;height:39px;line-height:37px}
.intro .btn-outline{left:219px;top:252px}

/* services */
.services{left:0;top:855px;width:1200px;height:360px;background:var(--white)}
.services h2{left:654px;top:36px;font-size:42px;font-weight:300}
.services h2 b{font-weight:700}
.services ul{left:657px;top:102px;list-style:none}
.services li{color:var(--blue);font-size:14px;line-height:30px}
.btn-gray{left:657px;top:273px;width:126px;height:36px;line-height:36px;background:#bdbdbd;color:var(--white);font-size:13px;text-align:center}

/* quote */
.quote{left:0;top:1215px;width:1200px;height:417px;background:linear-gradient(180deg,#2a93d6,#1f86cc)}
.quote h2{left:219px;top:24px;color:var(--white);font-size:38px;font-weight:300}
.quote h2 b{font-weight:700}
.quote .sub{left:219px;top:72px;color:#dcebf7;font-size:13px}
.field{position:absolute;height:36px;border:1px solid rgba(255,255,255,.55);background:rgba(255,255,255,.08);color:#e9f3fb;font-size:11px;padding:10px 8px}
.submit{left:219px;top:342px;width:132px;height:36px;line-height:36px;background:var(--white);color:var(--blue);font-size:12px;text-align:center}

/* projects */
.projects{left:0;top:1632px;width:1200px;height:753px;background:var(--light)}
.projects h2{left:213px;top:36px;font-size:40px;font-weight:300}
.projects h2 b{font-weight:700}
.btn-blue{left:543px;top:663px;width:126px;height:36px;line-height:36px;background:var(--blue);color:var(--white);font-size:13px;text-align:center}

/* testimonials */
.testimonials{left:0;top:2385px;width:1200px;height:351px;background:var(--white)}
.testimonials h2{left:222px;top:42px;font-size:40px;font-weight:700}
.tcard{position:absolute;top:120px;width:345px}
.tcard .mark{font-size:54px;line-height:30px;color:var(--blue);font-weight:700;float:left;margin-right:6px}
.tcard h3{color:var(--blue);font-size:19px;font-weight:600;line-height:40px}
.tcard p{clear:both;font-size:11px;line-height:16px;color:var(--muted);margin-top:12px}
.tcard .who{text-align:right;font-size:11px;color:var(--blue);margin-top:16px;padding-bottom:6px;border-bottom:1px solid var(--line)}

/* footer */
.footer{left:0;top:2736px;width:1200px;height:264px;background:linear-gradient(180deg,#1f5e96,#18497a)}
.fcol{position:absolute;top:57px;color:#d6e4f1;font-size:11px;line-height:18px}
.fcol h4{font-size:17px;font-weight:400;color:var(--white);margin-bottom:12px}
.crow{display:flex;align-items:flex-start;gap:10px;margin-bottom:10px}
.social{left:807px;top:102px;display:flex;gap:21px}
.social i{width:36px;height:36px;border-radius:50%;border:2px solid #cfdeee}
</style>
</head>
<body>

<header class="abs header">
  <div class="abs brand"><span class="brand-mark"></span><span class="brand-name">Bluefinch Painting</span></div>
  <div class="abs help">
    <div class="help-line">Need help? <b>(555) 318-7046</b></div>
    <div class="help-sub">Open Monday to Friday, 8AM to 5PM</div>
  </div>
</header>

<nav class="abs nav">
  <a class="active" style="left:216px;width:84px">Home</a>
  <a style="left:318px;width:72px">About</a>
  <a style="left:426px;width:90px">Services</a>
  <a style="left:549px;width:78px">Gallery</a>
  <a style="left:666px;width:90px">Contacts</a>
  <a class="cta" style="left:876px;width:117px">Free Quote</a>
</nav>

<section class="abs hero" role="img" aria-label="Photo of a freshly painted two-storey family home with a company trailer in the driveway"></section>
<div class="abs hero-title"><span>Commercial</span><br><span>&amp; residential painting</span></div>
<div class="abs dots"><i></i><i></i><i></i></div>

<section class="abs intro">
  <h2 class="abs">Quality painting<span>contractor</span></h2>
  <p class="abs">We are a family owned painting company serving home owners and businesses across the region. Our crew prepares every surface with care, protects your furniture and floors, and applies premium paints for a lasting finish. From a single room to a full exterior, we deliver clean lines, fair prices and work done on schedule every time.</p>
  <div class="abs btn-outline">Read More</div>
  <div class="ph" style="left:624px;top:36px;width:384px;height:258px;background:linear-gradient(135deg,#f4f4f4,#c9cfd4 60%,#7f8a80)" role="img" aria-label="Photo of the company's white work trailer with the business name and phone number"></div>
</section>

<section class="abs services">
  <div class="ph" style="left:219px;top:48px;width:393px;height:264px;background:linear-gradient(180deg,#f1f1ee,#d8d6d0)" role="img" aria-label="Photo of a sign reading We Proudly Use Quality Halden Coatings paints"></div>
  <h2 class="abs">Our <b>Services</b></h2>
  <ul class="abs">
    <li>- Lorem ipsum dolor sit amet conse ctetur</li>
    <li>- Adipisicing elit sed do eiusmod tempor</li>
    <li>- Incididunt ut labore dolore magna</li>
    <li>- Ut enim ad minim veniam quis nostrud</li>
    <li>- Exercitation Ulalmco laboris nisi</li>
  </ul>
  <div class="abs btn-gray">See All</div>
</section>

<section class="abs quote">
  <h2 class="abs"><b>Free</b> Quote</h2>
  <div class="abs sub">Just give us your details</div>
  <div class="field" style="left:219px;top:105px;width:228px">Your Name</div>
  <div class="field" style="left:459px;top:105px;width:225px">Email</div>
  <div class="field" style="left:219px;top:153px;width:228px">Phone Number</div>
  <div class="field" style="left:459px;top:153px;width:225px">City</div>
  <div class="field" style="left:219px;top:210px;width:465px;height:105px">Message</div>
  <div class="abs submit">Submit</div>
  <div class="ph" style="left:696px;top:135px;width:240px;height:282px;background:linear-gradient(160deg,rgba(40,120,200,0) 0%,#2f7fd0 40%,#d9a98a 85%);opacity:.85" role="img" aria-label="Photo of a hand holding a blue paint roller"></div>
</section>

<section class="abs projects">
  <h2 class="abs">Latest <b>Projects</b></h2>
  <div class="ph" style="left:213px;top:99px;width:387px;height:258px;background:linear-gradient(180deg,#cfe0ee,#8c8a7c 50%,#4f6a3e)" role="img" aria-label="Photo of a repainted grey house with a tidy front garden"></div>
  <div class="ph" style="left:618px;top:99px;width:387px;height:258px;background:linear-gradient(180deg,#9bbcd8,#7b7b72 50%,#dcdcdc)" role="img" aria-label="Photo of a house with a pickup truck and company trailer parked outside"></div>
  <div class="ph" style="left:213px;top:378px;width:387px;height:258px;background:linear-gradient(180deg,#9a9a96,#6d6c66 55%,#3f3f3a)" role="img" aria-label="Photo of a freshly painted back porch with large windows"></div>
  <div class="ph" style="left:618px;top:378px;width:387px;height:258px;background:linear-gradient(180deg,#dce8f1,#56734a 55%,#3d4a34)" role="img" aria-label="Photo of a painted house surrounded by tall trees"></div>
  <div class="abs btn-blue">See All</div>
</section>

<section class="abs testimonials">
  <h2 class="abs">Testimonials</h2>
  <div class="tcard" style="left:222px">
    <span class="mark">&ldquo;</span><h3>Lorem ipsum dolor sit</h3>
    <p>The crew arrived on time every morning, kept the yard clean and finished our exterior two days early. The colors look exactly as we hoped and the neighbors keep asking who did the work. We will gladly call them again next spring.</p>
    <div class="who">Client Name</div>
  </div>
  <div class="tcard" style="left:630px">
    <span class="mark">&ldquo;</span><h3>Lorem ipsum dolor sit</h3>
    <p>Friendly, careful and honest from the first estimate to the final walkthrough. They patched every crack, protected our floors and left sharp clean lines in every room. Great value and a finish that still looks brand new.</p>
    <div class="who">Client Name</div>
  </div>
</section>

<footer class="abs footer">
  <div class="fcol" style="left:228px">
    <h4>General Link</h4>
    Home<br>About<br>Service<br>Gallery<br>Contact<br>Site Map
  </div>
  <div class="fcol" style="left:405px">
    <h4>Our Services</h4>
    Service list 01<br>Service list 02<br>Service list 03<br>Service list 04<br>Service list 05
  </div>
  <div class="fcol" style="left:600px">
    <h4>Contact us</h4>
    <div class="crow">
      <svg width="12" height="16" viewBox="0 0 12 16"><path d="M6 0a6 6 0 0 0-6 6c0 4.5 6 10 6 10s6-5.5 6-10a6 6 0 0 0-6-6zm0 8.5A2.5 2.5 0 1 1 6 3.5a2.5 2.5 0 0 1 0 5z" fill="#fff"/></svg>
      <span>Office Address<br>1820 Alder Street<br>Lakeview, WA 98000</span>
    </div>
    <div class="crow">
      <svg width="14" height="14" viewBox="0 0 14 14"><path d="M3 0l3 3-2 2c1 2 3 4 5 5l2-2 3 3-2 3C6 14 0 8 0 3z" fill="#fff"/></svg>
      <span>(555) 318-7046</span>
    </div>
    <div class="crow">
      <svg width="14" height="10" viewBox="0 0 14 10"><rect x=".5" y=".5" width="13" height="9" fill="none" stroke="#fff"/><path d="M.5.5 7 6l6.5-5.5" fill="none" stroke="#fff"/></svg>
      <span>info@bluefinchpainting.example</span>
    </div>
  </div>
  <div class="abs social"><i></i><i></i><i></i></div>
</footer>

</body>
</html>
```